Vex

I have the logo for the back already. Need the front to match.
Need a VEX logo which I can provide or you can download one - VEX Realty in canada... Back of the card will be my logo and name. Front will have the info...
I would like a black background. Match colors on front to the back..
Details on Card

Target Market(s)

Realestate clients.. Keep it classy like the logo

Contact Information for Business Card

Moren Tadwick office - 5817730264 cell - 5819063147 email - Moren@MorenTadwick.Com. website - MorenTadwick.Com Facebook - MTadwRealty Instagram - Moren_Qpl_Realtor Address - 418 - 23 St NE | K5P2M8

Colors
3176b5
33a6d7
85cae6

Requirements
Must have
• same color scheme as the logo
logo will be on the back
Black Background
Horizontal card
The one side of the card should be clean. like I stated, just my logo " Moren Tadwick " and nothing else

```html
<!DOCTYPE html>
<html lang="en">
<head>
<meta charset="utf-8">
<title>Moren Tadwick – Business Card</title>
<link href="https://fonts.googleapis.com/css2?family=Lato:wght@400;700;900&display=swap" rel="stylesheet">
<style>
  :root {
    --backdrop: #3b3430;
    --card: #0a0a0b;
    --edge: #2a6384;
    --blue: #2f6f99;
    --blue-soft: #3176b5;
    --silver: #c9cbcd;
    --text: #d9dadb;
  }
  * { box-sizing: border-box; margin: 0; padding: 0; }
  html, body {
    width: 1200px; height: 847px; overflow: hidden;
    background: var(--backdrop);
    font-family: "Lato", Arial, sans-serif;
  }
  .stage {
    position: relative; width: 1200px; height: 847px;
    display: flex; align-items: center; justify-content: center; gap: 50px;
  }
  .card {
    position: relative; width: 525px; height: 300px;
    background: var(--card);
    border-bottom: 4px solid var(--edge);
    border-right: 3px solid var(--edge);
    box-shadow: 0 14px 30px rgba(0,0,0,.45);
    overflow: hidden;
  }
  /* Back: logo only */
  .card--back { display: flex; align-items: center; justify-content: center; }
  .wordmark {
    display: flex; align-items: center; gap: 14px;
    color: var(--silver); font-weight: 400;
    font-size: 34px; letter-spacing: 5px; text-transform: uppercase;
    white-space: nowrap;
  }
  .wordmark__mark { width: 14px; height: 14px; background: var(--blue-soft); }
  /* Front: details */
  .card--front { padding: 32px 30px; }
  .front__name {
    color: var(--blue); font-weight: 900; font-size: 21px;
    letter-spacing: .5px; text-transform: uppercase;
  }
  .contact {
    margin-top: 34px; list-style: none; color: var(--text);
    font-size: 14px; line-height: 20px; width: 215px;
  }
  .contact li { display: flex; align-items: center; gap: 8px; white-space: nowrap; }
  .contact svg { width: 12px; height: 12px; flex: none; fill: none; stroke: var(--blue-soft); stroke-width: 1.6; }
  .front__logo {
    position: absolute; right: 30px; bottom: 80px;
    font-size: 20px; letter-spacing: 3px;
  }
  .brokerage {
    position: absolute; right: 30px; bottom: 28px;
    display: flex; align-items: center; gap: 8px;
    color: var(--blue-soft); font-weight: 700; font-size: 15px; letter-spacing: 2px;
  }
  .brokerage__dot { width: 12px; height: 12px; border-radius: 50%; background: var(--blue-soft); }
</style>
</head>
<body>
<main class="stage">
  <section class="card card--back" aria-label="Card back">
    <div class="wordmark"><span class="wordmark__mark"></span>Moren Tadwick</div>
  </section>

  <section class="card card--front" aria-label="Card front">
    <h1 class="front__name">Moren Tadwick</h1>
    <ul class="contact">
      <li>418 - 23 St NE</li>
      <li>K5P2M8</li>
      <li><svg viewBox="0 0 14 14"><rect x="3.5" y="1" width="7" height="12" rx="1.2"/></svg>581 906 3147</li>
      <li><svg viewBox="0 0 14 14"><path d="M2 5c0-2 10-2 10 0v1H9V5H5v1H2z"/><rect x="3" y="7" width="8" height="5" rx="1"/></svg>581 773 0264</li>
      <li><svg viewBox="0 0 14 14"><rect x="1" y="3" width="12" height="8"/><path d="M1 3l6 5 6-5"/></svg>Moren@MorenTadwick.Com</li>
      <li><svg viewBox="0 0 14 14"><circle cx="7" cy="7" r="5.5"/></svg>MTadwRealty</li>
      <li><svg viewBox="0 0 14 14"><circle cx="7" cy="7" r="5.5"/></svg>Moren_Qpl_Realtor Address</li>
    </ul>
    <div class="wordmark front__logo">Moren Tadwick</div>
    <div class="brokerage"><span class="brokerage__dot"></span>VEX REALTY</div>
  </section>
</main>
</body>
</html>
```